Re-vamp existing website :www.tallowmerefinch.com.au

We need a new website design for this website
www.tallowmerefinch.com.au.

"creating financial lightbulb moments"

Looking for something modern, corporate like this https://www.pebbleharbor.com.au

Imagery is important, showing really great images of what we do.

We want to keep the theme of:
Build Your Future
Invest in your Dreams
Grow You

We want a blog/opinion page on the website

Staying with our three logo colours throughout

Industry/Entity Type

Financial Service

Number of Pages Required

5+ page

```html
<!DOCTYPE html>
<html lang="en">
<head>
<meta charset="utf-8">
<title>Tallowmere Finch – Creating Financial Lightbulb Moments</title>
<link rel="stylesheet" href="https://fonts.googleapis.com/css2?family=Oswald:wght@300;400;500&family=Open+Sans:wght@400;600;700&display=swap">
<style>
:root{
  --green:#93c94f;
  --teal:#4db5bb;
  --blue:#33a6dc;
  --ink:#222;
  --body:#555;
  --grey-icon:#9a9a9a;
  --red:#e2232b;
  --mist:#eef3f7;
  --paper:#f7f7f7;
  --footer:#262626;
  --footer-deep:#1b1b1b;
  --footer-text:#cfcfcf;
  --gold:#f1a51d;
  --brand-gradient:linear-gradient(180deg,var(--green) 0%,#7fc16c 45%,var(--teal) 100%);
}
*{box-sizing:border-box;margin:0;padding:0}
html,body{width:1200px;height:3139px;overflow:hidden;background:#fff}
body{position:relative;font-family:"Open Sans",Arial,sans-serif;color:var(--body)}
.abs{position:absolute}
.title-font{font-family:"Oswald","Arial Narrow",sans-serif}

/* header */
.site-header{left:0;top:0;width:1200px;height:119px;background:#fff}
.brand{left:73px;top:30px;display:flex;align-items:center;gap:14px}
.brand-dot{width:52px;height:52px;border-radius:50%;background:var(--blue)}
.brand-name{font-weight:700;font-size:30px;line-height:30px;color:var(--blue);width:170px}
.header-btn{left:1015px;width:116px;height:19px;font-size:7px;font-weight:700;color:#fff;text-transform:uppercase;display:flex;align-items:center;justify-content:center;letter-spacing:.3px}
.btn-login{top:34px;background:#6fb3dd}
.btn-register{top:67px;background:#a7cf2b}

.main-nav{left:0;top:119px;width:1200px;height:44px;background:var(--green);display:flex;justify-content:flex-end;align-items:center;padding-right:76px;gap:34px}
.main-nav a{color:#fff;text-decoration:none;font-size:17px}

/* hero */
.hero-photo{left:0;top:163px;width:1200px;height:438px;background:linear-gradient(100deg,#dfe6e3 0%,#f2efe9 35%,#e9ddd3 55%,#f4f2ef 80%,#e6ece8 100%)}
.hero-band{left:0;top:601px;width:1200px;height:285px;background:var(--brand-gradient)}
.band-title{color:#fff;font-weight:400;letter-spacing:3px;font-size:38px;line-height:44px}
.band-text{color:#fff;font-size:15.5px;line-height:19px;letter-spacing:.6px}
.outline-btn{width:162px;height:50px;border:2px solid #fff;border-radius:10px;color:#fff;font-weight:700;font-size:14px;display:flex;align-items:center;justify-content:center;letter-spacing:.4px}

/* services */
.service{width:160px;text-align:center;color:var(--red);font-size:16px;line-height:18px}
.service svg{display:block;margin:0 auto 8px}

/* about */
.about{left:0;top:1282px;width:1200px;height:393px;background:var(--mist)}
.section-title{width:1200px;text-align:center;color:var(--ink);font-weight:400}
.about-text{left:345px;top:1418px;width:535px;text-align:center;font-size:11px;line-height:22px;color:#444}
.solid-btn{width:158px;height:46px;border-radius:8px;background:#4fb3a4;color:#fff;font-weight:700;font-size:14px;display:flex;align-items:center;justify-content:center}

.journey{left:0;top:1675px;width:1200px;height:287px;background:var(--brand-gradient)}

/* blog */
.blog{left:0;top:1962px;width:1200px;height:446px;background:var(--paper)}
.date-col{width:52px;text-align:center;color:#222}
.date-day{font-weight:700;font-size:24px;line-height:24px}
.date-month{font-size:9px;margin-bottom:10px}
.date-stat{border-top:2px solid #e5c25a;padding-top:6px;font-size:8px;margin-bottom:10px}
.date-stat svg{display:block;margin:0 auto 2px}
.blog-photo{width:343px;height:166px;background:linear-gradient(120deg,#5a6a7a,#b8c3cc 55,#e6e9ec)}
.blog-photo.one{background:linear-gradient(120deg,#2f3a48 0%,#8b97a4 50%,#dfe3e7 100%)}
.blog-photo.two{background:linear-gradient(120deg,#1f2c3c 0%,#6f8294 45%,#d4dbe2 100%)}
.news-head{font-weight:700;font-size:10px;color:#111}
.news-text{font-size:10px;line-height:16px;color:#333;width:340px}

/* testimonials */
.testimonials{left:0;top:2408px;width:1200px;height:404px;background:#fff}
.quote-card{top:2544px;width:277px;height:140px;background:#fff;box-shadow:0 2px 8px rgba(0,0,0,.14);padding:16px 18px;font-size:9.5px;line-height:19px;color:#999}
.quote-mark{font-family:Georgia,serif;font-size:30px;color:#ccc;line-height:16px;float:left;margin-right:6px}
.arrow-btn{top:2480px;width:22px;height:22px;border:1px solid #bbb;background:#f3f3f3;display:flex;align-items:center;justify-content:center}
.reviewer{top:2700px;width:277px;display:flex;justify-content:flex-end;align-items:center;gap:10px;padding-right:20px;font-size:9.5px;color:#444}
.reviewer small{font-size:7px;color:#888}
.stars{color:var(--gold);font-size:9px;letter-spacing:1px;display:block;text-align:right}
.avatar{width:32px;height:36px;background:linear-gradient(#c9b8a6,#8b7a6b)}

/* footer */
.site-footer{left:0;top:2812px;width:1200px;height:327px;background:var(--footer)}
.footer-base{left:0;top:3078px;width:1200px;height:61px;background:var(--footer-deep)}
.footer-col{top:2858px;color:var(--footer-text)}
.footer-col h4{color:#fff;font-size:14px;font-weight:600;letter-spacing:.5px;padding-bottom:10px;position:relative;margin-bottom:18px}
.footer-col h4::after{content:"";position:absolute;left:0;bottom:0;width:28px;height:2px;background:var(--teal)}
.footer-col li{list-style:none;font-size:11px;line-height:27px;display:flex;align-items:center;gap:10px}
.footer-col li::before{content:"›";color:#fff;font-size:14px}
.footer-col.plain li::before{content:none}
.footer-divider{top:2860px;width:1px;height:180px;background:#444}
.social-ring{width:26px;height:26px;border:2px solid #ddd;border-radius:50%}
.copyright{left:0;top:3102px;width:1200px;text-align:center;font-size:10px;color:#ddd}
.copyright span{color:var(--blue)}
</style>
</head>
<body>

<header class="site-header abs">
  <div class="brand abs"><span class="brand-dot"></span><span class="brand-name">tallowmere finch</span></div>
  <div class="header-btn btn-login abs">Go to log in</div>
  <div class="header-btn btn-register abs">Register now</div>
</header>
<nav class="main-nav abs"><a>Home</a><a>About Us</a><a>Home Loans</a><a>Business Lending</a><a>Contact Us</a></nav>

<div class="hero-photo abs" role="img" aria-label="Photo of a mother working on a laptop on a sofa beside her young daughter, with thought bubbles of a couch and a tablet"></div>
<section class="hero-band abs">
  <h1 class="band-title title-font abs" style="left:280px;top:36px">CREATING FINANCIAL LIGHTBULB MOMENTS</h1>
  <p class="band-text abs" style="left:281px;top:96px;width:660px">Tallowmere Finch (TF) is a leading Australian finance brokerage group dedicated in providing our clients with a range of financial solutions tailored to their individual requirements. We want our clients to be bold in chasing their financial dreams and we commit to provide a range of opportunities for them to do so.</p>
  <div class="outline-btn abs" style="left:519px;top:201px">TELL ME MORE</div>
</section>

<section class="services">
  <div class="service abs" style="left:324px;top:968px">
    <svg width="66" height="60" viewBox="0 0 66 60"><circle cx="16" cy="14" r="10" fill="none" stroke="#9a9a9a" stroke-width="6"/><circle cx="50" cy="46" r="10" fill="none" stroke="#9a9a9a" stroke-width="6"/><line x1="52" y1="4" x2="14" y2="56" stroke="#9a9a9a" stroke-width="7"/></svg>Rates</div>
  <div class="service abs" style="left:519px;top:968px">
    <svg width="66" height="60" viewBox="0 0 66 60"><rect x="6" y="4" width="54" height="38" rx="3" fill="none" stroke="#9a9a9a" stroke-width="5"/><rect x="28" y="42" width="10" height="9" fill="#9a9a9a"/><rect x="18" y="51" width="30" height="5" fill="#9a9a9a"/></svg>eServices</div>
  <div class="service abs" style="left:714px;top:968px">
    <svg width="66" height="60" viewBox="0 0 66 60"><rect x="14" y="2" width="38" height="54" rx="3" fill="#9a9a9a"/><rect x="19" y="7" width="28" height="11" fill="#fff"/><g fill="#fff"><rect x="19" y="23" width="7" height="6"/><rect x="30" y="23" width="7" height="6"/><rect x="41" y="23" width="6" height="6"/><rect x="19" y="33" width="7" height="6"/><rect x="30" y="33" width="7" height="6"/><rect x="41" y="33" width="6" height="6"/><rect x="19" y="43" width="7" height="6"/><rect x="30" y="43" width="7" height="6"/><rect x="41" y="43" width="6" height="6"/></g></svg>Calculators</div>
  <div class="service abs" style="left:324px;top:1098px">
    <svg width="66" height="60" viewBox="0 0 66 60"><rect x="28" y="2" width="10" height="22" fill="#9a9a9a"/><polygon points="18,22 48,22 33,38" fill="#9a9a9a"/><path d="M10 34 V54 H56 V34 H46 V44 H20 V34Z" fill="#9a9a9a"/></svg>Tools</div>
  <div class="service abs" style="left:519px;top:1098px">
    <svg width="66" height="60" viewBox="0 0 66 60"><g fill="#9a9a9a"><rect x="12" y="4" width="30" height="8" rx="2"/><rect x="12" y="15" width="30" height="8" rx="2"/><rect x="12" y="26" width="30" height="8" rx="2"/><rect x="12" y="37" width="26" height="8" rx="2"/><circle cx="44" cy="44" r="14"/></g><text x="44" y="50" font-size="16" font-weight="700" fill="#fff" text-anchor="middle" font-family="Arial,sans-serif">$</text></svg>Patronage<br>Dividend</div>
  <div class="service abs" style="left:714px;top:1098px">
    <svg width="66" height="60" viewBox="0 0 66 60"><rect x="14" y="2" width="38" height="54" rx="3" fill="none" stroke="#9a9a9a" stroke-width="5"/><rect x="21" y="12" width="24" height="6" fill="#9a9a9a"/><rect x="21" y="24" width="24" height="6" fill="#9a9a9a"/><rect x="21" y="36" width="24" height="6" fill="#9a9a9a"/></svg>More...</div>
</section>

<section class="about abs"></section>
<h2 class="section-title title-font abs" style="left:0;top:1304px;font-size:42px">ABOUT US</h2>
<p class="about-text abs">Our brokers compare lenders across the market to find the loan that suits you. We take time to learn your goals, your income and your plans, then explain every option in plain words. From a first home to a growing business, we stay beside you at each step, review your loans each year and help you keep more of what you earn for the future.</p>
<div class="solid-btn abs" style="left:521px;top:1581px">TELL ME MORE</div>

<section class="journey abs">
  <h2 class="band-title title-font abs" style="left:282px;top:44px">START YOUR JOURNEY</h2>
  <p class="band-text abs" style="left:282px;top:101px;width:640px">Find the right loan and repayment structure for you – it could save you thousands over the life of a loan. Get access to exclusive home loan offers and we'll help you negotiate a competitive deal. Talking to a person who gets it really makes a difference.</p>
  <div class="outline-btn abs" style="left:519px;top:204px">TELL ME MORE</div>
</section>

<section class="blog abs"></section>
<h2 class="section-title abs" style="left:0;top:1986px;font-size:22px;font-family:'Open Sans',Arial,sans-serif">BLOG</h2>

<div class="date-col abs" style="left:157px;top:2072px">
  <div class="date-day">24</div><div class="date-month">Nov-2015</div>
  <div class="date-stat"><svg width="20" height="16" viewBox="0 0 20 16"><path d="M3 2h14v9H8l-4 4v-4H3z" fill="none" stroke="#333" stroke-width="2"/></svg>8- Com</div>
  <div class="date-stat"><svg width="20" height="14" viewBox="0 0 20 14"><ellipse cx="10" cy="7" rx="9" ry="5" fill="none" stroke="#333" stroke-width="2"/><circle cx="10" cy="7" r="2.5" fill="#333"/></svg>16- View</div>
</div>
<div class="blog-photo one abs" style="left:224px;top:2077px" role="img" aria-label="Photo of business people meeting around a table"></div>
<div class="news-head abs" style="left:224px;top:2270px">NEWS HEADING</div>
<p class="news-text abs" style="left:224px;top:2288px">Rates moved again this month. Here is what the change means for your repayments and when a refinance may help you save.</p>

<div class="date-col abs" style="left:601px;top:2072px">
  <div class="date-day">24</div><div class="date-month">Nov-2015</div>
  <div class="date-stat"><svg width="20" height="16" viewBox="0 0 20 16"><path d="M3 2h14v9H8l-4 4v-4H3z" fill="none" stroke="#333" stroke-width="2"/></svg>8- Com</div>
  <div class="date-stat"><svg width="20" height="14" viewBox="0 0 20 14"><ellipse cx="10" cy="7" rx="9" ry="5" fill="none" stroke="#333" stroke-width="2"/><circle cx="10" cy="7" r="2.5" fill="#333"/></svg>16- View</div>
</div>
<div class="blog-photo two abs" style="left:666px;top:2077px" role="img" aria-label="Photo of hands reviewing financial charts on paper and a tablet"></div>
<div class="news-head abs" style="left:666px;top:2270px">NEWS HEADING</div>
<p class="news-text abs" style="left:666px;top:2288px">Small business owners have more lending choices than ever. We explain how to compare offers and pick the right structure.</p>

<section class="testimonials abs"></section>
<h2 class="section-title abs" style="left:0;top:2462px;font-size:24px;font-weight:600;font-family:'Open Sans',Arial,sans-serif">Testimonials</h2>
<div class="arrow-btn abs" style="left:988px"><svg width="8" height="10" viewBox="0 0 8 10"><path d="M6 1L2 5l4 4" fill="none" stroke="#666" stroke-width="1.6"/></svg></div>
<div class="arrow-btn abs" style="left:1014px"><svg width="8" height="10" viewBox="0 0 8 10"><path d="M2 1l4 4-4 4" fill="none" stroke="#666" stroke-width="1.6"/></svg></div>

<div class="quote-card abs" style="left:159px"><span class="quote-mark">“</span>The team found us a better rate and explained every step clearly. Our home loan was approved fast and the whole process felt easy.</div>
<div class="quote-card abs" style="left:461px"><span class="quote-mark">“</span>The team found us a better rate and explained every step clearly. Our home loan was approved fast and the whole process felt easy.</div>
<div class="quote-card abs" style="left:762px"><span class="quote-mark">“</span>The team found us a better rate and explained every step clearly. Our home loan was approved fast and the whole process felt easy.</div>

<div class="reviewer abs" style="left:159px"><div>Mara Lintel, <small>Hobart</small><span class="stars">★★★★★</span></div><div class="avatar" role="img" aria-label="Reviewer portrait"></div></div>
<div class="reviewer abs" style="left:461px"><div>Mara Lintel, <small>Hobart</small><span class="stars">★★★★★</span></div><div class="avatar" role="img" aria-label="Reviewer portrait"></div></div>
<div class="reviewer abs" style="left:762px"><div>Mara Lintel, <small>Hobart</small><span class="stars">★★★★★</span></div><div class="avatar" role="img" aria-label="Reviewer portrait"></div></div>

<footer class="site-footer abs"></footer>
<div class="footer-base abs"></div>
<div class="footer-divider abs" style="left:293px"></div>
<div class="footer-divider abs" style="left:544px"></div>
<div class="footer-divider abs" style="left:800px"></div>

<div class="footer-col abs" style="left:151px"><h4>QUICK LINKS</h4><ul><li>Home</li><li>About Us</li><li>Offering</li><li>Blog</li><li>Contact Us</li></ul></div>
<div class="footer-col abs" style="left:356px"><h4>SUPPORT</h4><ul><li>Terms and Conditions</li><li>FAQ</li><li>Partner Hub</li><li>Affiliate Program</li></ul></div>
<div class="footer-col plain abs" style="left:603px"><h4>CONTACT US</h4><ul>
  <li><svg width="10" height="14" viewBox="0 0 10 14"><path d="M5 0a5 5 0 0 1 5 5c0 4-5 9-5 9S0 9 0 5a5 5 0 0 1 5-5z" fill="#fff"/><circle cx="5" cy="5" r="2" fill="#262626"/></svg>Harrowgate Finance Co.</li>
  <li style="padding-left:20px">Level 4, 120 Harbour St</li>
  <li style="padding-left:20px">Hobart TAS 7000</li>
  <li><svg width="12" height="12" viewBox="0 0 12 12"><path d="M2 0l3 3-1.5 2a7 7 0 0 0 3.5 3.5L9 7l3 3-2 2C5 12 0 7 0 2z" fill="#fff"/></svg>0800-555-0142</li>
  <li><svg width="12" height="9" viewBox="0 0 12 9"><rect width="12" height="9" fill="#fff"/><path d="M0 0l6 5 6-5" fill="none" stroke="#262626"/></svg><span style="color:var(--blue)">hello@tallowmerefinch.com.au</span></li>
</ul></div>
<div class="footer-col plain abs" style="left:842px"><h4>FOLLOW US</h4><ul style="line-height:35px">
  <li style="line-height:35px"><span class="social-ring"></span>Chatterbook</li>
  <li style="line-height:35px"><span class="social-ring"></span>Chirpline</li>
  <li style="line-height:35px"><span class="social-ring"></span>Orbit Plus</li>
  <li style="line-height:35px"><span class="social-ring"></span>Linkwell</li>
</ul></div>

<p class="copyright abs">Copyright © <span>Finchline Studio</span> 2015. All Rights Reserved</p>

</body>
</html>
```